Construction material supplies company business card ****

1. Full company name “Marlow Aggregate Products Ltd”
I am after a Business card design for the company as a whole. We are better known in Solomon Islands as “Marlow Aggregate” for short.

We are a building materials supplier of
Ready Mixed Concrete, Bricks and Blocks,
Quarry products- gravel, aggregates, sand etc.
Cement distributor/retailer of reputable brands.
Other prefab concrete products. Culverts, wave breakers, concrete retaining blocks etc.

2. Competitive Advantage over Competition: Quality, efficient, professional, dependable, reliable

3. We want people to feel trust worthy, high quality, strong when they see our brand

5. No preference to color. Maybe more sturdy and corporate. Not fancy.

Industry/Entity Type

CONSTRUCTION SUPPLY

Contact Information for Business Card

Name, Position, office phone mob phone, email

Requirements
Must have
• the company logo
Nice to have
• would like to see a mixture of designs, of with logo only and also with simple graphic designs to bring out the company whilst still have the strong sturdy professional feeling

```html
<!DOCTYPE html>
<html lang="en">
<head>
<meta charset="utf-8">
<title>Marlow Aggregate – Business Card</title>
<link href="https://fonts.googleapis.com/css2?family=Michroma&family=Lato:wght@400;700&display=swap" rel="stylesheet">
<style>
  :root {
    --navy: #12446a;
    --white: #ffffff;
    --backdrop: #a3a3a3;
    --rule: #6d6d6d;
    --ink: #222222;
  }
  * { margin: 0; padding: 0; box-sizing: border-box; }
  html, body {
    width: 1132px; height: 1200px; overflow: hidden;
    background: var(--backdrop);
  }
  .canvas { position: relative; width: 1132px; height: 1200px; }

  .card {
    position: absolute; left: 215px; width: 702px; height: 401px;
  }
  .card--front { top: 151px; background: var(--navy); }
  .card--back { top: 647px; background: var(--white); }

  .wordmark {
    display: flex; align-items: center; gap: 10px;
    font-family: "Michroma", sans-serif; font-weight: 400;
    letter-spacing: 0.5px; white-space: nowrap;
  }
  .wordmark__mark { display: block; }

  .card--front .wordmark {
    position: absolute; right: 70px; top: 305px;
    color: var(--white); font-size: 17px;
  }
  .card--front .wordmark__mark { width: 18px; height: 18px; background: var(--white); }

  .card--back .wordmark {
    position: absolute; left: 30px; width: 320px; top: 228px;
    justify-content: center;
    color: var(--navy); font-size: 18px;
  }
  .card--back .wordmark__mark { width: 20px; height: 20px; background: var(--navy); }

  .divider {
    position: absolute; left: 377px; top: 156px;
    width: 2px; height: 129px; background: var(--rule);
  }
  .contact {
    position: absolute; left: 398px; top: 157px;
    font-family: "Lato", sans-serif; color: var(--ink);
  }
  .contact__name {
    font-family: "Michroma", sans-serif; font-weight: 400;
    font-size: 18px; color: var(--navy); letter-spacing: 1px;
    line-height: 26px;
  }
  .contact__role, .contact__company {
    font-size: 14px; line-height: 18px; font-weight: 700;
  }
  .contact__role { margin-top: 2px; }
  .contact__list { list-style: none; margin-top: 12px; }
  .contact__item {
    display: flex; align-items: center; gap: 8px;
    font-size: 14px; line-height: 19px; font-weight: 700;
  }
  .contact__icon { width: 11px; height: 11px; fill: var(--navy); flex: none; }
</style>
</head>
<body>
<main class="canvas">
  <section class="card card--front" aria-label="Card front">
    <div class="wordmark">
      <span class="wordmark__mark"></span>
      <span class="wordmark__name">MARLOW AGGREGATE</span>
    </div>
  </section>

  <section class="card card--back" aria-label="Card back">
    <div class="wordmark">
      <span class="wordmark__mark"></span>
      <span class="wordmark__name">MARLOW AGGREGATE</span>
    </div>
    <div class="divider"></div>
    <div class="contact">
      <h1 class="contact__name">DANIEL HARPER</h1>
      <p class="contact__role">Founder and CEO</p>
      <p class="contact__company">Marlow Aggregate Products Ltd</p>
      <ul class="contact__list">
        <li class="contact__item">
          <svg class="contact__icon" viewBox="0 0 24 24"><path d="M6.6 10.8a15.1 15.1 0 0 0 6.6 6.6l2.2-2.2a1 1 0 0 1 1-.25 11.4 11.4 0 0 0 3.6.57 1 1 0 0 1 1 1V20a1 1 0 0 1-1 1A17 17 0 0 1 3 4a1 1 0 0 1 1-1h3.5a1 1 0 0 1 1 1c0 1.25.2 2.45.57 3.57a1 1 0 0 1-.25 1z"/></svg>
          <span>000 000 0000</span>
        </li>
        <li class="contact__item">
          <svg class="contact__icon" viewBox="0 0 24 24"><path d="M7 1h10a2 2 0 0 1 2 2v18a2 2 0 0 1-2 2H7a2 2 0 0 1-2-2V3a2 2 0 0 1 2-2zm0 3v15h10V4z"/></svg>
          <span>000 000 0000</span>
        </li>
        <li class="contact__item">
          <svg class="contact__icon" viewBox="0 0 24 24"><path d="M2 5h20v14H2zm2 2v.5l8 5 8-5V7z"/></svg>
          <span>info@marlowaggregate.com.au</span>
        </li>
      </ul>
    </div>
  </section>
</main>
</body>
</html>
```